Web Design Project - ReelHarbor Style Website

Hi there, we want to create a ReelHarbor / Flickden style website. We have a logo, and will be using a similar structure to this platform; http://tapecrate.example/v2/
Please feel free to be creative as possible, and make the site look however you would like :) keeping in mind the Ad space, and user friendly layout. We would like
1) The main page and
2) the video view page
designed
Updates
Logo and stock image uploaded
Hello; we most likely be basing the site on this tape crate theme, which also works as a mobile version.
Another option that I found for a layout which is different :)
http://www.quillnest-studio.example/demo-theme.cfm?theme=marvane
One last update; really like this one too
I am 100% likely to now use this format;
Target Market(s)
Bars, Cafe's, Restaurants, Attractions, Venues, Pubs, Wine and Dine
Industry/Entity Type
Reelharbor
Requirements
Must have
- Can be similar to ReelHarbor, but closer to Flickden's funky fresh look.
Should not have
- Not be too cluttered with too many videos on the home page. Feel free to think outside the box

```html
<!DOCTYPE html>
<html lang="en">
<head>
<meta charset="utf-8">
<title>Tablereel</title>
<link rel="stylesheet" href="https://fonts.googleapis.com/css2?family=PT+Sans:wght@400;700&family=Arimo:wght@400;700&display=swap">
<style>
  :root {
    --ink: #0a0a0a;
    --header: #1c1c1c;
    --band: #b9b8b4;
    --paper: #e2e1de;
    --sky: #3dd3f8;
    --nav-text: #ffffff;
    --nav-active: #29b9ea;
    --panel-dark: #333333;
    --field: #ffffff;
    --field-border: #c9c9c9;
    --muted: #9a9a9a;
    --pill: #4a4a4a;
  }
  * { box-sizing: border-box; margin: 0; padding: 0; }
  html, body { width: 1130px; height: 1200px; overflow: hidden; }
  body {
    position: relative;
    background: var(--paper);
    font-family: "Arimo", Arial, sans-serif;
    color: var(--ink);
  }
  .abs { position: absolute; }
  .backdrop { left: 0; top: 0; width: 1130px; height: 1200px; }

  .site-header { left: 0; top: 0; width: 1130px; height: 119px; background: linear-gradient(#262626, #111); }
  .header-band { left: 0; top: 119px; width: 1130px; height: 17px; background: var(--band); }
  .brand {
    left: 190px; top: 34px; color: #fff;
    font-family: "PT Sans", sans-serif; font-weight: 700; font-size: 56px; line-height: 1;
    display: flex; align-items: center; gap: 14px;
  }
  .brand-mark { width: 30px; height: 30px; background: #fff; }
  .account-btn {
    height: 24px; border-radius: 5px; background: var(--pill); color: #fff;
    font-family: "PT Sans", sans-serif; font-size: 11px;
    display: flex; align-items: center; justify-content: center;
    box-shadow: inset 0 1px 0 rgba(255,255,255,.15);
  }

  .frame { left: 176px; top: 160px; width: 818px; height: 998px; background: var(--ink); }
  .main-nav {
    left: 169px; top: 167px; width: 832px; height: 42px;
    background: linear-gradient(#252525, #151515);
    border-bottom: 1px solid #333;
  }
  .main-nav a {
    position: absolute; top: 14px; color: var(--nav-text); text-decoration: none;
    font-weight: 700; font-size: 11px; letter-spacing: .1px; white-space: nowrap;
  }
  .main-nav a.active { color: var(--nav-active); }
  .caret { font-size: 11px; margin-left: 5px; }

  .hero { left: 194px; top: 233px; width: 786px; height: 364px; background: var(--panel-dark); }
  .hero-media { left: 208px; top: 242px; width: 481px; height: 347px;
    background: radial-gradient(circle at 50% 45%, #c88d3e 0%, #8e4c1c 55%, #4a2310 100%); }
  .play { left: 411px; top: 390px; width: 58px; height: 58px; }
  .hero-copy {
    left: 702px; top: 242px; width: 268px; height: 346px;
    background: radial-gradient(circle at 50% 40%, #b3b3b0, #8f8f8c);
    font-family: "PT Sans", sans-serif;
  }
  .hero-copy h1 { position: absolute; left: 21px; top: 21px; font-size: 24px; line-height: 28px; font-weight: 700; color: #111; white-space: nowrap; }
  .hero-copy h1 span { display: block; color: #fff; margin-left: 3px; }
  .hero-copy p { position: absolute; left: 29px; top: 88px; font-size: 9px; line-height: 17px; font-weight: 700; color: #111; white-space: nowrap; }
  .learn-more { position: absolute; left: 30px; top: 302px; width: 136px; height: 26px;
    background: linear-gradient(#2b2b2b, #0c0c0c); color: #fff; font-size: 11px; font-weight: 700;
    display: flex; align-items: center; justify-content: center; }

  .thumb-strip { left: 169px; top: 625px; width: 832px; height: 77px; background: linear-gradient(#222, #141414); }
  .thumb { top: 637px; width: 98px; height: 52px; border: 2px solid #d8d8d8; }
  .strip-arrow { top: 645px; color: #777; font-size: 32px; font-family: "PT Sans", sans-serif; line-height: 1; }

  .content { left: 185px; top: 702px; width: 803px; height: 407px; background: var(--paper); }
  .divider { left: 203px; top: 738px; width: 770px; height: 2px; background: #fff; border-top: 1px solid #ccc; }
  .reply-title { left: 200px; top: 762px; font-size: 17px; font-weight: 700; letter-spacing: .6px; color: #111; }
  .field { left: 200px; width: 160px; height: 24px; background: var(--field); border: 1px solid var(--field-border); }
  .field-label { left: 364px; font-size: 11px; color: #111; }
  .req { color: #e01b1b; margin-left: 4px; }
  .message { left: 200px; top: 906px; width: 487px; height: 139px; background: var(--field); border: 1px solid var(--field-border); }
  .post-btn { left: 200px; top: 1061px; width: 82px; height: 23px; background: #000; color: #fff; font-size: 12px;
    display: flex; align-items: center; justify-content: center; }

  .site-footer { left: 169px; top: 1109px; width: 832px; height: 44px; background: linear-gradient(#252525, #151515); }
  .copyright { left: 188px; top: 1127px; color: var(--muted); font-size: 10.5px; }
  .social { top: 1118px; width: 29px; height: 29px; border-radius: 4px; }
</style>
</head>
<body>
  <svg class="abs backdrop" viewBox="0 0 1130 1200" aria-hidden="true">
    <polygon points="0,424 1130,305 1130,611 0,742" fill="var(--sky)"/>
  </svg>

  <header class="abs site-header"></header>
  <div class="abs header-band"></div>
  <div class="abs brand"><span class="brand-mark"></span>Tablereel</div>
  <div class="abs account-btn" style="left:681px;top:36px;width:90px;">Upload video</div>
  <div class="abs account-btn" style="left:784px;top:37px;width:90px;">Member Login</div>
  <div class="abs account-btn" style="left:888px;top:36px;width:90px;">Create Account</div>

  <div class="abs frame"></div>
  <nav class="abs main-nav">
    <a class="active" style="left:35px;">HOME</a>
    <a style="left:102px;">LAYOUTS<span class="caret">▼</span></a>
    <a style="left:202px;">BLOG</a>
    <a style="left:267px;">SHORTCODES<span class="caret">▼</span></a>
    <a style="left:394px;">PORTFOLIO<span class="caret">▼</span></a>
    <a style="left:505px;">CONTACT</a>
  </nav>

  <section class="abs hero"></section>
  <div class="abs hero-media" role="img" aria-label="Featured video still: warm-lit restaurant dining room with set tables"></div>
  <svg class="abs play" viewBox="0 0 58 58" aria-hidden="true">
    <circle cx="29" cy="29" r="27" fill="rgba(20,20,20,.75)" stroke="#111" stroke-width="3"/>
    <polygon points="23,19 39,29 23,39" fill="#ddd"/>
  </svg>
  <div class="abs hero-copy">
    <h1>YOUR LATEST VIDEO<span>PUSH LINE HERE</span></h1>
    <p>Lorem ipsum dolor sit amet, cinsectetuer adispicing<br>elit. Nam cursus. Morbi ut mi. Nullam enim leo,<br>edges id., condimentum at, laoreet mattis, massa.<br>Sed eleiferend nonummy diaam.<br>Lorem ipsum dolor sit amet, cinsectetuer adispicing<br>elit. Nam cursus. Morbi ut mi. Nullam enim leo,<br>edges id., condimentum at, laoreet mattis, massa.<br>Sed eleiferend nonummy diaam.<br>Lorem ipsum dolor sit amet, cinsectetuer adispicing<br>elit. Nam cursus. Morbi ut mi. Nullam enim leo,<br>edges id., condimentum at, laoreet mattis, massa.<br>Sed eleiferend nonummy diaam.</p>
    <div class="learn-more">Learn More</div>
  </div>

  <div class="abs thumb-strip"></div>
  <div class="abs strip-arrow" style="left:186px;">‹</div>
  <div class="abs thumb" style="left:211px;background:linear-gradient(135deg,#7a5a22,#3a2410);" role="img" aria-label="Video thumbnail: bistro interior"></div>
  <div class="abs thumb" style="left:319px;background:linear-gradient(135deg,#c9c3bd,#5a3a32);" role="img" aria-label="Video thumbnail: cafe seating"></div>
  <div class="abs thumb" style="left:427px;background:linear-gradient(135deg,#2a1f2a,#b86a20);" role="img" aria-label="Video thumbnail: bar at night"></div>
  <div class="abs thumb" style="left:535px;background:linear-gradient(135deg,#a88e6c,#4e3a26);" role="img" aria-label="Video thumbnail: dining hall"></div>
  <div class="abs thumb" style="left:643px;background:linear-gradient(135deg,#c98a3a,#5a3210);" role="img" aria-label="Video thumbnail: table setting"></div>
  <div class="abs thumb" style="left:751px;background:linear-gradient(135deg,#5a5a66,#201c22);" role="img" aria-label="Video thumbnail: restaurant lounge"></div>
  <div class="abs thumb" style="left:859px;background:linear-gradient(135deg,#c9d0cc,#9a7a5a);" role="img" aria-label="Video thumbnail: function room"></div>
  <div class="abs strip-arrow" style="left:970px;">›</div>

  <main class="abs content"></main>
  <div class="abs divider"></div>
  <h2 class="abs reply-title">LEAVE A REPLY</h2>
  <div class="abs field" style="top:800px;"></div>
  <div class="abs field-label" style="top:806px;">Name<span class="req">*</span></div>
  <div class="abs field" style="top:836px;"></div>
  <div class="abs field-label" style="top:843px;">Email<span class="req">*</span></div>
  <div class="abs field" style="top:871px;"></div>
  <div class="abs field-label" style="top:877px;">Website</div>
  <div class="abs message"></div>
  <div class="abs post-btn">Post</div>

  <footer class="abs site-footer"></footer>
  <div class="abs copyright">Copyright @ Ledgerline</div>
  <div class="abs social" style="left:877px;background:#f08a1c;" role="img" aria-label="Feed link"></div>
  <div class="abs social" style="left:913px;background:#3a5a9a;" role="img" aria-label="Social link"></div>
  <div class="abs social" style="left:950px;background:#e8e8e8;" role="img" aria-label="Social link"></div>
</body>
</html>
```